Computer consultant business card

Brimlo Software is a newly started computer consulting company. It's a small one-man company that provides mostly Velunix applications but also websites in collaboration with designers. I'm running this company on the side of full time university studies.

I want the final design to be clean and memorable. Be creative! :)

Some inspiration:
http://www.tavelpix.net/design/73519
http://www.tavelpix.net/design/2739566/business-card-design-by-quillbop
http://www.tavelpix.net/design/804613/business-card-design-by-lorvena-brukwaldsen

See attachment for my company logo.
Updates

I would like to thank everyone for submitting! I'll need a couple of days to review and ultimately select a design.

Target Market(s)

Non-technical entrepreneurs and small companies.

Industry/Entity Type

University

Requirements
Must have
• My company logo.
In any way, both colors from my logo.
First- and last name, e-mail and phone number.
Double-sided design.
Nice to have
• Something creative with the symbol in my logo

```html
<!DOCTYPE html>
<html lang="en">
<head>
<meta charset="utf-8">
<title>Brimlo Software – Business Card</title>
<link rel="stylesheet" href="https://fonts.googleapis.com/css2?family=Quicksand:wght@400;500;600&display=swap">
<style>
  :root {
    --brand-blue: #8ee3f8;
    --brand-black: #060909;
    --bg-light: #cfd9d9;
    --bg-dark: #a7b6b6;
    --divider: #eef2f2;
    --text-dark: #111414;
  }
  * { margin: 0; padding: 0; box-sizing: border-box; }
  html, body {
    width: 1041px;
    height: 1200px;
    overflow: hidden;
  }
  body {
    position: relative;
    font-family: "Quicksand", sans-serif;
    background: radial-gradient(ellipse 60% 45% at 50% 27%, var(--bg-light), var(--bg-dark)) top / 100% 600px no-repeat,
                radial-gradient(ellipse 60% 45% at 50% 75%, var(--bg-light), var(--bg-dark)) bottom / 100% 600px no-repeat;
  }
  .card-side {
    position: absolute;
    left: 0;
    width: 1041px;
    height: 600px;
  }
  .card-front { top: 0; }
  .card-back { top: 600px; }

  .band {
    position: absolute;
    box-shadow: 0 6px 10px rgba(0, 0, 0, 0.35);
  }
  .band-black { background: var(--brand-black); }
  .band-blue { background: var(--brand-blue); }

  .front-band { left: 0; top: 232px; width: 795px; height: 134px; }
  .front-mark { left: 801px; top: 232px; width: 240px; height: 134px; }

  .wordmark {
    position: absolute;
    left: 378px;
    top: 246px;
    font-size: 96px;
    font-weight: 600;
    line-height: 1;
    color: var(--brand-blue);
    letter-spacing: 1px;
  }

  .mark-dot {
    position: absolute;
    left: 50%;
    top: 50%;
    width: 106px;
    height: 106px;
    margin: -53px 0 0 -53px;
    border-radius: 50%;
    background: var(--brand-black);
  }

  .divider {
    position: absolute;
    left: 86px;
    top: 599px;
    width: 871px;
    height: 1px;
    background: var(--divider);
    z-index: 2;
  }

  .name-band { left: 0; top: 234px; width: 410px; height: 132px; }
  .back-mark { left: 801px; top: 234px; width: 240px; height: 132px; }

  .holder-name {
    position: absolute;
    left: 36px;
    top: 34px;
    font-size: 58px;
    font-weight: 400;
    line-height: 1.1;
    color: var(--brand-blue);
    letter-spacing: 1px;
    word-spacing: 10px;
  }

  .contact-list {
    position: absolute;
    left: 428px;
    top: 254px;
    list-style: none;
    color: var(--text-dark);
    font-size: 25px;
    font-weight: 500;
    letter-spacing: -0.5px;
  }
  .contact-list li { line-height: 1; margin-bottom: 32px; }
  .contact-label { margin-right: 8px; }
</style>
</head>
<body>
  <section class="card-side card-front" aria-label="Front of card">
    <div class="band band-black front-band"></div>
    <div class="wordmark">brimlo</div>
    <div class="band band-blue front-mark"><span class="mark-dot"></span></div>
  </section>

  <div class="divider"></div>

  <section class="card-side card-back" aria-label="Back of card">
    <div class="band band-black name-band">
      <p class="holder-name">Your Name</p>
    </div>
    <ul class="contact-list">
      <li><span class="contact-label">Phone :</span> 1234567890</li>
      <li><span class="contact-label">Email :</span> yourname@mail.com</li>
    </ul>
    <div class="band band-blue back-mark"><span class="mark-dot"></span></div>
  </section>
</body>
</html>
```